Brightwell Systems - Company Overview Brochure

We would like a single page A4 Brochure to give to new potential customers to provide a quick overview of our company. This will be used in presales meetings.

We have included the content we would like on the brochure under "Brightwell Systems Marketing Brochure.docx".

We have included two other designs "timebundleterms v4.pdf and Brightwell Public Cloud Plans.pdf" which shows similar marketing brochures we have. We would like these designs to have the same Brightwell Blue and "Specialised Technology Consultancy firm" theme.

Target Market(s)

Technology Sector

Industry/Entity Type

Information Technology

Colors
0054AA
0677BA
7BADD7
CADEEF
E8F1F8

Requirements
Must have
• "Innovative Tech Company Theme".

```html
<!DOCTYPE html>
<html lang="en">
<head>
<meta charset="utf-8">
<title>Brightwell Systems – Company Overview</title>
<link rel="stylesheet" href="https://fonts.googleapis.com/css2?family=Montserrat:wght@400;500;600;700;800&display=swap">
<style>
:root{
  --page-bg:#c9c9c9;
  --navy-deep:#0f1a55;
  --navy:#1a2c82;
  --navy-mid:#203a9a;
  --brand-blue:#1e7fd0;
  --sky:#7badd7;
  --ice:#cadeef;
  --mist:#e8f1f8;
  --white:#ffffff;
  --ink:#1b2a7a;
  --panel-line:rgba(123,173,215,.55);
}
*{margin:0;padding:0;box-sizing:border-box}
html,body{width:1200px;height:2573px;overflow:hidden;background:var(--page-bg);font-family:"Montserrat",sans-serif}
.sheet{position:absolute;left:50px;top:508px;width:1100px;height:1556px;background:linear-gradient(160deg,var(--navy-mid) 0%,var(--navy) 45%,var(--navy-deep) 100%);box-shadow:0 10px 30px rgba(0,0,0,.25);overflow:hidden;color:var(--white)}
.header{position:absolute;left:0;top:0;width:100%;height:154px;background:var(--white)}
.header-texture{position:absolute;right:0;top:0;width:240px;height:154px;background:linear-gradient(90deg,rgba(232,241,248,0) 0%,var(--mist) 100%)}
.brand{position:absolute;left:84px;top:54px;display:flex;align-items:center;gap:16px}
.brand-mark{width:46px;height:46px;border-radius:50%;background:var(--ink)}
.brand-name{font-weight:700;font-size:34px;color:var(--ink);letter-spacing:1px}
.header-divider{position:absolute;left:520px;top:56px;width:3px;height:42px;background:var(--ink)}
.header-title{position:absolute;left:596px;top:58px;font-weight:700;font-size:29px;color:var(--ink);letter-spacing:.5px;white-space:nowrap}
.headline{position:absolute;left:64px;top:172px;font-weight:800;font-size:98px;line-height:94px;letter-spacing:1px}
.headline .accent{color:var(--brand-blue);display:block}
.intro{position:absolute;left:64px;top:418px;width:640px;font-size:20px;line-height:27px;text-align:justify}
.service-box{position:absolute;top:541px;width:474px;height:433px;border:2px solid var(--panel-line);background:linear-gradient(180deg,rgba(255,255,255,.06),rgba(255,255,255,.02))}
.service-box.it{left:63px}
.service-box.security{left:576px}
.box-title{height:104px;display:flex;align-items:center;justify-content:center;text-align:center;font-weight:700;font-size:22px;line-height:26px;border-bottom:1px solid var(--panel-line);background:rgba(255,255,255,.05)}
.box-grid{display:grid;grid-template-columns:1fr 1fr;grid-template-rows:1fr 1fr;height:327px;padding:14px 10px}
.service{display:flex;flex-direction:column;align-items:center;justify-content:center;text-align:center;font-size:17px;line-height:19px;font-weight:500;gap:10px}
.service svg{width:56px;height:56px}
.lower{position:absolute;left:63px;top:1010px;width:987px;height:290px}
.policy{position:absolute;left:0;top:0;width:480px}
.commitment{position:absolute;left:548px;top:0;width:440px}
.split{position:absolute;left:500px;top:30px;width:2px;height:260px;background:var(--panel-line)}
.section-title{font-weight:800;font-size:29px;margin-bottom:20px}
.commitment .section-title{color:var(--brand-blue)}
.policy-item{display:flex;gap:20px;margin-bottom:18px}
.policy-item svg{flex:0 0 56px;width:56px;height:56px;margin-top:24px}
.policy-item h3{color:var(--brand-blue);font-weight:600;font-size:22px;margin-bottom:6px}
.policy-item p,.commitment p{font-size:12.6px;line-height:15.4px}
.policy-rule{border-top:1px dashed var(--panel-line);margin:0 0 14px 76px}
.commitment p{margin-bottom:14px}
.terms{position:absolute;left:0;top:1333px;width:100%;height:81px;background:var(--navy-deep);display:flex;align-items:center;justify-content:center;text-align:center;font-size:17px;line-height:21px;color:var(--brand-blue);padding:0 120px}
.terms strong{color:var(--white);font-weight:500}
.contact{position:absolute;left:0;top:1454px;width:100%;height:102px;display:flex;align-items:center;justify-content:center;gap:30px;font-size:18px;font-weight:500;background:linear-gradient(90deg,var(--navy-deep),var(--navy))}
.contact-item{display:flex;align-items:center;gap:10px}
.contact-item svg{width:24px;height:24px}
</style>
</head>
<body>
<main class="sheet">
  <header class="header">
    <div class="header-texture" role="img" aria-label="Faint light-blue tech line pattern"></div>
    <div class="brand"><span class="brand-mark"></span><span class="brand-name">BRIGHTWELL</span></div>
    <span class="header-divider"></span>
    <h2 class="header-title">SPECIALISED CONSULTING</h2>
  </header>

  <h1 class="headline">DO IT ONCE<span class="accent">DO IT RIGHT</span></h1>
  <p class="intro">Brightwell Systems is a Technology Consulting Company based in Perth, Western Australia, which offers customers tailored technical solutions for a range of products.</p>

  <section class="service-box it">
    <div class="box-title">IT SERVICES</div>
    <div class="box-grid">
      <div class="service"><svg viewBox="0 0 56 56" fill="#fff"><circle cx="28" cy="14" r="9"/><rect x="16" y="26" width="24" height="26" rx="4"/></svg>Project<br>Intergration</div>
      <div class="service"><svg viewBox="0 0 56 56" fill="none" stroke="#fff" stroke-width="4" stroke-linecap="round"><path d="M6 26l12-10 10 6 10-6 12 10"/><path d="M16 30l10 10 4-4 6 4 8-10"/></svg>Managed<br>Services</div>
      <div class="service"><svg viewBox="0 0 56 56"><path d="M18 26v-8a10 10 0 0 1 20 0v8" fill="none" stroke="#fff" stroke-width="4"/><rect x="12" y="26" width="32" height="24" rx="3" fill="#fff"/><circle cx="28" cy="37" r="3" fill="#1a2c82"/></svg>Enterprise<br>Security</div>
      <div class="service"><svg viewBox="0 0 56 56" fill="none" stroke="#fff" stroke-width="3"><rect x="6" y="10" width="38" height="30" rx="2"/><path d="M20 20l-5 5 5 5M30 20l5 5-5 5"/><circle cx="44" cy="42" r="7"/></svg>Software<br>Development</div>
    </div>
  </section>

  <section class="service-box security">
    <div class="box-title">ELECTRONIC SECURITY &amp;<br>COMMUNICATION</div>
    <div class="box-grid">
      <div class="service"><svg viewBox="0 0 56 56" fill="#fff"><rect x="10" y="14" width="32" height="14" rx="3" transform="rotate(15 26 21)"/><rect x="22" y="32" width="4" height="14"/><rect x="12" y="44" width="16" height="4"/></svg>CCTV</div>
      <div class="service"><svg viewBox="0 0 56 56"><path d="M28 4l20 8v14c0 12-9 22-20 26C17 48 8 38 8 26V12z" fill="#fff"/><path d="M30 14l-8 14h6l-2 12 8-16h-6z" fill="#1a2c82"/></svg>Intergrated<br>Electronic Security</div>
      <div class="service"><svg viewBox="0 0 56 56" fill="none" stroke="#fff" stroke-width="4" stroke-linecap="round"><path d="M16 6v18c0 8 6 12 12 12s12-4 12-12V6"/><path d="M28 6v30M28 36v16"/></svg>Structured Cabling<br>&amp; Fibre Optics</div>
      <div class="service"><svg viewBox="0 0 56 56" fill="none" stroke="#fff" stroke-width="3.5" stroke-linecap="round"><circle cx="28" cy="26" r="4" fill="#fff"/><path d="M20 18a11 11 0 0 0 0 16M36 18a11 11 0 0 1 0 16M13 11a21 21 0 0 0 0 30M43 11a21 21 0 0 1 0 30"/><path d="M28 30v20"/></svg>Wireless<br>Communications</div>
    </div>
  </section>

  <section class="lower">
    <div class="policy">
      <h2 class="section-title">OUR POLICY</h2>
      <div class="policy-item">
        <svg viewBox="0 0 56 56" fill="none" stroke="#7badd7" stroke-width="3"><path d="M28 6v44M14 50h28M8 14h40"/><path d="M14 14l-8 16h16zM42 14l-8 16h16z"/></svg>
        <div><h3>Be Fair</h3><p>At Brightwell we believe that both parties benefit when pricing is fair. If margins are too low, we may sacrifice service quality, and this ultimately harms our brand. If margins are too high, our customers have an incentive to seek alternative providers, and this compromises our growth and damages client relationships.</p></div>
      </div>
      <div class="policy-rule"></div>
      <div class="policy-item">
        <svg viewBox="0 0 56 56" fill="#7badd7"><rect x="8" y="36" width="8" height="16"/><rect x="20" y="28" width="8" height="24"/><rect x="32" y="20" width="8" height="32"/><path d="M8 26L30 10l4 4 10-8v10h-4V12l-10 8-4-4L10 30z"/></svg>
        <div><h3>Be Cost-Effective</h3><p>At Brightwell we believe that it is possible to deliver both high quality at a fair cost, by providing services that are intelligent and efficient</p></div>
      </div>
    </div>
    <span class="split"></span>
    <div class="commitment">
      <h2 class="section-title">OUR COMMITMENT</h2>
      <p>Our commitment to you is to do things right the first time while being fair but cost-effective. If you're looking for the cheapest consultants, Brightwell may not be the right fit for you.</p>
      <p>We are a specialised consultancy firm that offers tailored solutions to government and the enterprise sector with some of Perth's best consultants.</p>
      <p>In areas such as cybersecurity and business continuity, it pays to get it done correctly the first time in alignment with vendor best practices. There are many ways of doing things in the technology field, and only after understanding all methods of achieving an outcome can you recommend the best solution in alignment with best practices.</p>
    </div>
  </section>

  <p class="terms"><span>All goods and services provided by Brightwell are provided in accordance with our Standard Terms and Conditions available at <strong>https://www.brightwellsystems.com.au/t&amp;c</strong></span></p>

  <footer class="contact">
    <span class="contact-item"><svg viewBox="0 0 24 24"><circle cx="12" cy="12" r="12" fill="#1e7fd0"/><path d="M8 6l3 3-2 2c1 2 2 3 4 4l2-2 3 3-2 2c-5 0-10-5-10-10z" fill="#fff"/></svg>0891234567</span>
    <span class="contact-item"><svg viewBox="0 0 24 24"><circle cx="12" cy="12" r="12" fill="#1e7fd0"/><rect x="6" y="8" width="12" height="9" fill="#fff"/><path d="M6 8l6 5 6-5" fill="none" stroke="#1e7fd0" stroke-width="1.5"/></svg>sales@brightwellsystems.com.au</span>
    <span class="contact-item"><svg viewBox="0 0 24 24"><circle cx="12" cy="12" r="12" fill="#1e7fd0"/><circle cx="12" cy="12" r="6" fill="none" stroke="#fff" stroke-width="1.5"/><path d="M6 12h12M12 6c-3 3-3 9 0 12M12 6c3 3 3 9 0 12" fill="none" stroke="#fff" stroke-width="1.2"/></svg>www.brightwellsystems.com.au</span>
  </footer>
</main>
</body>
</html>
```